Brantor Energy Services Website - Solar Sales and Installation and Renewable Energy Marketing

I need a website for my solar sales and installation/renewable energy marketing company. We will focus on solar, so the web page should make that a main focus. Ideally it will have 5-6 total pages. One main page, one page "Why Solar", "Our Services", "About Us", "Contact Us", and some type of page that collects leads or information from customers who are interested in a solar quote. Our image focus should be either residential solar panels or windmills (renewable energy). The logo, attached, is green and orange. The color scheme should be predominantly white, clean cut, with orange/green buttons or accents. I don't want to have a blog-like page, it should mimic other solar company websites. A good example would be Calderby's solar website.

```html
<!DOCTYPE html>
<html lang="en">
<head>
<meta charset="utf-8">
<title>Brantor Energy Services</title>
<link href="https://fonts.googleapis.com/css2?family=Raleway:wght@500;600;700&family=Open+Sans:wght@400;600&display=swap" rel="stylesheet">
<style>
:root{
  --green:#5fc81f;
  --green-dark:#3f9a12;
  --green-soft:#eef8e6;
  --orange:#f39a1e;
  --text:#333;
  --muted:#666;
  --dark:#2b2b2b;
  --white:#fff;
}
*{box-sizing:border-box;margin:0;padding:0}
html,body{width:1200px;height:2808px;overflow:hidden;background:var(--white)}
body{font-family:"Open Sans",sans-serif;color:var(--text);position:relative}
h1,h2,h3{font-family:"Raleway",sans-serif}

.site-header{position:absolute;top:0;left:0;width:1200px;height:84px;display:flex;align-items:center;justify-content:space-between;padding:0 40px;background:var(--white);box-shadow:0 2px 8px rgba(0,0,0,.06);z-index:5}
.brand{display:flex;align-items:center;gap:12px;font-family:"Raleway",sans-serif;font-weight:700;font-size:16px;color:var(--green-dark);line-height:1.1;width:150px}
.brand-dot{width:36px;height:36px;border-radius:50%;background:var(--orange);flex:none}
.main-nav{display:flex;gap:14px}
.main-nav a{font-family:"Raleway",sans-serif;font-weight:600;font-size:17px;color:var(--dark);text-decoration:none;padding:10px 14px}
.main-nav a.active{border-bottom:3px solid var(--green)}

.hero{position:absolute;top:84px;left:0;width:1200px;height:420px;background:var(--white);overflow:hidden}
.hero-swoosh{position:absolute;left:0;top:0}
.hero-copy{position:absolute;left:40px;top:44px;width:520px}
.hero-copy h1{font-size:58px;line-height:1.08;color:var(--green);font-weight:700}
.hero-copy p{font-size:22px;line-height:1.4;color:var(--dark);margin-top:22px;font-weight:600;width:440px}
.btn{display:inline-block;background:var(--green);color:var(--white);font-family:"Raleway",sans-serif;font-weight:700;font-size:17px;padding:12px 22px;text-decoration:none;border-radius:2px}
.hero-copy .btn{margin-top:26px;color:var(--dark)}
.hero-photo{position:absolute;left:580px;top:0;width:580px;height:420px;background:linear-gradient(160deg,#9cc9ee 0%,#3b5c86 40%,#c9b8a0 70%,#8f7b62 100%)}

.intro{position:absolute;top:580px;left:120px;width:960px;text-align:center;font-size:22px;line-height:1.72;color:var(--dark)}
.intro strong{color:var(--orange);font-weight:600}

.benefits{position:absolute;top:810px;left:0;width:1200px;height:360px}
.benefits-photo{position:absolute;left:0;top:0}
.benefits-copy{position:absolute;left:605px;top:66px}
.benefits-copy h2{font-size:40px;color:var(--green);font-weight:600;margin-bottom:24px}
.benefits-copy ul{list-style:none}
.benefits-copy li{font-size:19px;line-height:1.75;color:var(--dark)}

.why{position:absolute;top:1230px;left:0;width:1200px}
.section-title{display:flex;align-items:center;justify-content:center;gap:22px;font-size:40px;color:var(--green);font-weight:600}
.section-title::before,.section-title::after{content:"";width:120px;height:2px;background:var(--green)}
.features{display:grid;grid-template-columns:440px 440px;column-gap:120px;row-gap:46px;justify-content:center;margin-top:40px}
.feature{text-align:center}
.feature svg{display:block;margin:0 auto 10px}
.feature h3{font-size:24px;color:var(--orange);font-weight:700;margin-bottom:14px}
.feature p{font-size:16px;line-height:1.7;color:var(--dark)}

.quote{position:absolute;top:1848px;left:0;width:1200px;height:532px;background:linear-gradient(180deg,#e2d6c6 0%,#b89a78 35%,#6c6c74 70%,#3f4f66 100%)}
.quote-form{position:absolute;left:200px;top:128px;width:800px;height:368px;background:rgba(255,255,255,.94);padding:28px 48px}
.quote-form h2{font-size:36px;color:var(--green);font-weight:600;text-align:center;margin-bottom:26px}
.form-grid{display:grid;grid-template-columns:1fr 1fr;column-gap:40px;row-gap:12px}
.field label{display:block;font-size:14px;color:var(--dark);margin-bottom:6px}
.field span{display:block;height:28px;background:var(--green-soft);border:1px solid #d8ead0}
.field.full{grid-column:1/3}
.send{position:absolute;right:48px;bottom:26px;background:var(--green);color:var(--dark);font-weight:700;font-size:14px;padding:8px 20px}

.contact{position:absolute;top:2380px;left:0;width:1200px;height:388px;background:var(--green)}
.contact-copy{position:absolute;left:110px;top:64px;width:420px;color:var(--white)}
.contact-copy h2{font-size:40px;font-weight:600;display:flex;align-items:center;gap:16px}
.contact-copy h2::before,.contact-copy h2::after{content:"";width:60px;height:2px;background:var(--white)}
.contact-copy p{font-size:17px;line-height:1.6;margin-top:26px}
.contact-list{list-style:none;margin-top:30px}
.contact-list li{display:flex;align-items:center;gap:18px;font-size:17px;line-height:1;margin-bottom:18px}
.contact-map{position:absolute;left:600px;top:32px;width:540px;height:250px;background:linear-gradient(135deg,#e8efe3 0%,#cfe1f2 60%,#a9c9e6 100%);border:1px solid #ccc}

.site-footer{position:absolute;top:2768px;left:0;width:1200px;height:40px;background:var(--dark);color:#ddd;font-size:14px;text-align:center;line-height:40px}
</style>
</head>
<body>

<header class="site-header">
  <div class="brand"><span class="brand-dot"></span>Brantor Energy Services</div>
  <nav class="main-nav">
    <a href="#" class="active">Home</a>
    <a href="#">Why Solar</a>
    <a href="#">Our Services</a>
    <a href="#">About Us</a>
    <a href="#">Contact Us</a>
  </nav>
</header>

<section class="hero">
  <svg class="hero-swoosh" width="1200" height="420" viewBox="0 0 1200 420">
    <path d="M0 300 C220 260 420 420 620 330 L620 420 L0 420 Z" fill="#eef8e6"/>
    <path d="M420 40 C520 120 560 220 520 420 L600 420 C640 220 560 100 470 20 Z" fill="#f3faee"/>
  </svg>
  <div class="hero-copy">
    <h1>Experience Energy Independence. Go Solar.</h1>
    <p>We provide sales and installation of high quality solar energy systems.</p>
    <a href="#" class="btn">Request A Free Quote</a>
  </div>
  <div class="hero-photo" role="img" aria-label="Photo of a smiling couple seated in front of a house with rooftop solar panels"></div>
</section>

<p class="intro">The sun provides enough energy a day to power the whole planet for a year, you don't have to keep paying those exorbitant fees on utility bills when you can harness the free energy of the sun and make the earth a greener planet at the same time. At <strong>BRANTOR ENERGY SERVICES</strong>, we provide sustainable energy solutions for your homes and workplace alike.</p>

<section class="benefits">
  <svg class="benefits-photo" width="560" height="360" viewBox="0 0 560 360" role="img" aria-label="Photo of a technician installing solar panels on a roof">
    <defs>
      <linearGradient id="roofGrad" x1="0" y1="0" x2="1" y2="1">
        <stop offset="0" stop-color="#5d8fc7"/>
        <stop offset="0.5" stop-color="#2d4f80"/>
        <stop offset="1" stop-color="#1e2f4a"/>
      </linearGradient>
    </defs>
    <polygon points="0,0 420,0 560,360 0,360" fill="url(#roofGrad)"/>
  </svg>
  <div class="benefits-copy">
    <h2>Benefits Of Going Solar</h2>
    <ul>
      <li>-Unlimited amount of energy</li>
      <li>-Huge savings on utility bills</li>
      <li>-Low maintenance cost</li>
      <li>-Increase in the resale value of your home</li>
      <li>-Become part of creating a greener planet</li>
    </ul>
  </div>
</section>

<section class="why">
  <h2 class="section-title">Why Choose Us?</h2>
  <div class="features">
    <div class="feature">
      <svg width="48" height="44" viewBox="0 0 48 44"><rect x="4" y="4" width="40" height="26" fill="none" stroke="#f39a1e" stroke-width="3"/><path d="M4 17H44M17 4V30M31 4V30M24 30V40M14 40H34" stroke="#f39a1e" stroke-width="3"/></svg>
      <h3>High Efficiency Solar Panels</h3>
      <p>We provide state of the art solar panels that are designed with modern nano technology to provide efficient energy conversion.</p>
    </div>
    <div class="feature">
      <svg width="48" height="44" viewBox="0 0 48 44"><circle cx="24" cy="16" r="9" fill="none" stroke="#f39a1e" stroke-width="3"/><path d="M13 12H35M8 42C8 30 16 27 24 27S40 30 40 42" fill="none" stroke="#f39a1e" stroke-width="3"/></svg>
      <h3>Professional Installation Technicians</h3>
      <p>Our team of highly skilled and certified technicians are readily available to design and install your energy systems in the layout that best fits your home with safety being emphasized.</p>
    </div>
    <div class="feature">
      <svg width="48" height="44" viewBox="0 0 48 44"><rect x="6" y="10" width="36" height="28" fill="none" stroke="#f39a1e" stroke-width="3"/><path d="M14 10V5H20V10M28 10V5H34V10M14 24H20M31 21V27M28 24H34" stroke="#f39a1e" stroke-width="3"/></svg>
      <h3>Durable Inverter Systems And Batteries</h3>
      <p>We also provide power efficient inverters and high quality batteries with a long lifespan and deep charge cycle.</p>
    </div>
    <div class="feature">
      <svg width="48" height="44" viewBox="0 0 48 44"><circle cx="24" cy="22" r="17" fill="none" stroke="#f39a1e" stroke-width="3"/><path d="M16 22L22 28L33 16" fill="none" stroke="#f39a1e" stroke-width="3"/></svg>
      <h3>Overall Guaranteed Performance</h3>
      <p>With a warranty period of up to 20 years, our solar energy systems are guaranteed to serve you reliably with very little maintenance required over it's life span.</p>
    </div>
  </div>
</section>

<section class="quote" role="img" aria-label="Background photo of a roof covered with solar panels">
  <form class="quote-form">
    <h2 class="section-title">Request A Free Quote</h2>
    <div class="form-grid">
      <div class="field"><label>First Name</label><span></span></div>
      <div class="field"><label>Last Name</label><span></span></div>
      <div class="field"><label>Phone Number</label><span></span></div>
      <div class="field"><label>Zip Code</label><span></span></div>
      <div class="field full"><label>Email</label><span></span></div>
    </div>
    <span class="send">SEND &#10140;</span>
  </form>
</section>

<section class="contact">
  <div class="contact-copy">
    <h2>Contact Us</h2>
    <p>If you have any questions or further inquiries you can reach us via one of the links below.</p>
    <ul class="contact-list">
      <li><svg width="22" height="22" viewBox="0 0 24 24"><path d="M6 2L10 6L8 9C9 12 12 15 15 16L18 14L22 18L19 22C10 21 3 14 2 5Z" fill="#fff"/></svg>(555) 010-2400</li>
      <li><svg width="22" height="22" viewBox="0 0 24 24"><rect x="6" y="1" width="12" height="22" rx="2" fill="#fff"/><rect x="8" y="4" width="8" height="14" fill="#5fc81f"/></svg>(555) 010-2401</li>
      <li><svg width="22" height="22" viewBox="0 0 24 24"><rect x="2" y="5" width="20" height="14" fill="#fff"/><path d="M2 5L12 13L22 5" fill="none" stroke="#5fc81f" stroke-width="2"/></svg>info@brantorenergyservices.com</li>
    </ul>
  </div>
  <div class="contact-map" role="img" aria-label="Map showing the office location"></div>
</section>

<footer class="site-footer">Copyright ©Brantor Energy Services</footer>

</body>
</html>
```